Meridel Capra SA Business Cards

Dear all,
Thank you for reading my brief and project. My company is doing doing advisory in real estate and to comapnies + real estates services as asset management, brokerage, development etc.
I would like to get a business card for my company which is clear, professionnal and serious.
Please have a look to the attachement to see the logos of the company

Industry/Entity Type

Real Estate

Contact Information for Business Card

I would like to have in the business card the following
Principal side:
- Logo of the company (or Monogram)
- First and Last Name (Paulo Vestrand)
- Mobile number
- email address

Second side:
- Address (Chemin des Orvets 17, 1226 Thônex - Switzerland)
- website (www.meridelcapra.ch)

Requirements
Must have
• Refer to the typeface and logo colors

```html
<!DOCTYPE html>
<html lang="en">
<head>
<meta charset="utf-8">
<title>Meridel Capra SA – Business Card</title>
<link href="https://fonts.googleapis.com/css2?family=Poppins:wght@300;400;500&display=swap" rel="stylesheet">
<style>
  :root {
    --page-bg: #e8e5e1;
    --ink-dark: #3a4350;
    --ink-text: #4a4f57;
    --brand-blue: #0a74bd;
    --rule-grey: #6f7883;
    --front-light: #ffffff;
    --front-shade: #cdcdcd;
    --back-deep: #1c2430;
    --back-mid: #3c4a5a;
    --white: #ffffff;
    --white-soft: rgba(255,255,255,0.82);
  }
  * { box-sizing: border-box; margin: 0; padding: 0; }
  html, body {
    width: 1125px; height: 1200px; overflow: hidden;
    background: var(--page-bg);
    font-family: "Poppins", sans-serif;
  }
  .canvas { position: relative; width: 1125px; height: 1200px; }
  .card {
    position: absolute; left: 150px; width: 826px; height: 472px;
    box-shadow: 0 4px 10px rgba(0,0,0,0.25);
  }
  .card--front {
    top: 98px;
    background: linear-gradient(90deg, var(--front-light) 0%, var(--front-light) 42%, var(--front-shade) 100%);
  }
  .card--back {
    top: 631px;
    background: linear-gradient(90deg, var(--back-deep) 0%, var(--back-mid) 62%, var(--back-mid) 100%);
  }
  .brand-block { position: absolute; left: 398px; top: 58px; height: 106px; display: flex; align-items: center; }
  .brand-square { width: 56px; height: 56px; background: var(--ink-dark); }
  .brand-divider { width: 2px; height: 106px; margin-left: 40px; background: linear-gradient(180deg, transparent, var(--brand-blue) 30%, var(--brand-blue) 70%, transparent); }
  .brand-name {
    margin-left: 32px; font-weight: 500; font-size: 25px; letter-spacing: 0.5px;
    color: var(--ink-dark); white-space: nowrap;
  }
  .person { position: absolute; left: 52px; top: 300px; }
  .person-name { font-weight: 500; font-size: 24px; color: var(--brand-blue); line-height: 1.05; letter-spacing: 0.3px; }
  .person-role { font-weight: 400; font-size: 20px; color: var(--ink-text); line-height: 1.15; }
  .rule { position: absolute; left: 52px; right: 56px; top: 362px; height: 2px; background: var(--rule-grey); }
  .contact { position: absolute; left: 52px; top: 378px; font-weight: 300; font-size: 19px; color: var(--ink-text); line-height: 25px; }
  .contact-key { color: var(--brand-blue); font-weight: 400; }
  .website { position: absolute; right: 56px; top: 378px; font-weight: 300; font-size: 19px; color: var(--ink-dark); line-height: 25px; }
  .back-details {
    position: absolute; left: 52px; bottom: 52px;
    font-weight: 300; font-size: 17px; line-height: 25px; color: var(--white-soft);
  }
  .back-brand { position: absolute; right: 56px; bottom: 56px; display: flex; align-items: center; gap: 12px; }
  .back-square { width: 20px; height: 20px; background: var(--white); }
  .back-name { font-weight: 500; font-size: 20px; color: var(--white); letter-spacing: 0.5px; }
</style>
</head>
<body>
<main class="canvas">
  <section class="card card--front" aria-label="Business card front">
    <div class="brand-block">
      <div class="brand-square"></div>
      <div class="brand-divider"></div>
      <div class="brand-name">MERIDEL CAPRA</div>
    </div>
    <div class="person">
      <p class="person-name">PAULO VESTRAND</p>
      <p class="person-role">President</p>
    </div>
    <div class="rule"></div>
    <div class="contact">
      <p><span class="contact-key">c</span>.369-480-2715</p>
      <p><span class="contact-key">e</span>.info@meridelcapra.ch</p>
    </div>
    <p class="website">www.meridelcapra.ch</p>
  </section>
  <section class="card card--back" aria-label="Business card back">
    <address class="back-details" style="font-style: normal;">
      <p>Chemin des Orvets 17</p>
      <p>1226 Thônex – Switzerland</p>
      <p>www.meridelcapra.ch</p>
    </address>
    <div class="back-brand">
      <div class="back-square"></div>
      <span class="back-name">MERIDEL CAPRA</span>
    </div>
  </section>
</main>
</body>
</html>
```